Cd Cover design for Chicago based record label.

Cd Cover design for a new single! Song is dedicated to exotic dancers. We do not want our artist pictures on this one. So please use your imagination. Song Title: "Velvet Hours". Thanks? Artist: Ray Castellan feat. Lil Trevane.

```html
<!DOCTYPE html>
<html lang="en">
<head>
<meta charset="utf-8">
<title>Velvet Hours – Ray Castellan feat. Lil Trevane</title>
<link href="https://fonts.googleapis.com/css2?family=Advent+Pro:wght@200;300&family=Courier+Prime:wght@700&display=swap" rel="stylesheet">
<style>
  :root {
    --backdrop: #262b2e;
    --cover-dark: #0c0c0c;
    --cover-mid: #1c1c1c;
    --title-grey: #b9b9b9;
    --pole-grey: #a9a9a9;
    --artist-white: #d8d8d8;
    --accent-olive: #b3b026;
    --figure-light: #eeeeee;
  }
  html, body {
    margin: 0;
    padding: 0;
    width: 1200px;
    height: 799px;
    overflow: hidden;
    background: var(--backdrop);
  }
  .stage {
    position: relative;
    width: 1200px;
    height: 799px;
  }
  .cover {
    position: absolute;
    left: 240px;
    top: 40px;
    width: 720px;
    height: 720px;
    background: radial-gradient(circle at 35% 30%, var(--cover-mid) 0%, var(--cover-dark) 75%);
    overflow: hidden;
  }
  .cover-art {
    position: absolute;
    inset: 0;
  }
  .title {
    position: absolute;
    right: 290px;
    top: 210px;
    margin: 0;
    font-family: "Advent Pro", sans-serif;
    font-weight: 200;
    font-size: 148px;
    line-height: 132px;
    letter-spacing: 2px;
    color: var(--title-grey);
    text-align: right;
    text-transform: uppercase;
  }
  .title span { display: block; }
  .credits {
    position: absolute;
    right: 290px;
    top: 500px;
    text-align: right;
    font-family: "Courier Prime", monospace;
    font-weight: 700;
  }
  .artist {
    margin: 0;
    font-size: 30px;
    letter-spacing: 1px;
    color: var(--artist-white);
  }
  .featuring {
    margin: 2px 0 0;
    font-size: 20px;
    color: var(--accent-olive);
  }
</style>
</head>
<body>
<main class="stage">
  <section class="cover">
    <svg class="cover-art" width="720" height="720" viewBox="0 0 720 720">
      <defs>
        <linearGradient id="dancerTone" x1="0" y1="0" x2="1" y2="1">
          <stop offset="0" stop-color="var(--accent-olive)" stop-opacity="0.55"/>
          <stop offset="0.5" stop-color="var(--figure-light)" stop-opacity="0.35"/>
          <stop offset="1" stop-color="var(--accent-olive)" stop-opacity="0.45"/>
        </linearGradient>
      </defs>
      <rect class="dancer-illustration" x="450" y="70" width="250" height="430" rx="40"
            fill="url(#dancerTone)" role="img"
            aria-label="Silhouette of a pole dancer inverted in a split, white figure with olive heels, shorts and hair"/>
      <g class="pole" stroke="var(--pole-grey)" stroke-width="5" stroke-linecap="butt">
        <line x1="470" y1="90" x2="470" y2="300"/>
        <line x1="470" y1="520" x2="470" y2="600"/>
      </g>
    </svg>
    <h1 class="title"><span>Velvet</span><span>Hours</span></h1>
    <div class="credits">
      <p class="artist">Ray Castellan</p>
      <p class="featuring">feat. Lil Trevane</p>
    </div>
  </section>
</main>
</body>
</html>
```